Integrative Medical Practice Website Redo

I am needing to have our current website redesigned to make it a responsive website to work on smartphones.
Current website
www.brightoakfm.com
Here are several examples of what I am looking for
https://www.thymecarehub.com/
I am wanting a popup for a newsletter signup
Looking for a very professional, clean, simple, minimalist, bold well designed website
Colors would ideally be greens and blues, cool tones, muted colors, or graytones like:
https://journeybalance.org/
Several other clean design examples
http://9anchorsboulder.com/
http://www.velumedical.com/
http://sproutyouth.com/
http://ourcellcastle.com/
I would like the top navigation bar to be able to slide down while browsing site
We are also needing to add several features that are not on our current website:
Questionnaire buttons
Are you toxic questionnaire?
Take our hormone quiz to find out if hormones are affecting your health.
online scheduling option for:
nutrition counselling
testing like body composition, basal metabolic rate, CIMT, breast thermography, VO2 Max testing, Vita Beat
Therapies like whole body vibration, infrared sauna, Exercise with oxygen, hyperbaric oxygen, spinal decompression
Need to have separate page for different services and split up services into:
Consults/Office Visits, Testing, Therapies, Procedures
Need to have a button link to patient portal
Needs to have online store
Need to add navigation button "Start Here"
Need a spot for a video on practice summary
Newsletter signup to collect emails
Testimonials from facebook
Blog that posts can be shared with social media
Password protected patient access that can integrate into crate.io ideally
Modules for programs online classes/videos
I have attached stock images that you can use, but feel free to find others to use.
I have also attached a copy of our current brochure that shows an overview of the practice
Target Market(s)
Health conscious people of all ages looking for a family medicine doctor
Industry/Entity Type
Alternative Medicine
Coding
Coded - Design and coding required
Number of Pages Required
5+ page

```html
<!DOCTYPE html>
<html lang="en">
<head>
<meta charset="utf-8">
<title>Bright Oak Family Medicine</title>
<link href="https://fonts.googleapis.com/css2?family=Cinzel:wght@400&family=Open+Sans:ital,wght@0,400;0,600;1,400&display=swap" rel="stylesheet">
<style>
  :root {
    --brand-blue: #2f9fd6;
    --heading-blue: #2a8cc4;
    --navy: #1d4f7a;
    --ink: #2b2b2b;
    --body-text: #444;
    --muted-bg: #ececec;
    --rule: #d6d6d6;
    --green: #5aa02c;
    --green-light: #8cc63f;
    --card-border: #c9dd8a;
    --icon: #3d3d3d;
    --white: #fff;
  }
  * { box-sizing: border-box; margin: 0; padding: 0; }
  html, body { width: 901px; height: 1200px; overflow: hidden; }
  body { position: relative; background: var(--white); font-family: "Open Sans", Arial, sans-serif; color: var(--ink); }

  .top-bar { position: absolute; left: 0; top: 0; width: 901px; height: 22px; background: var(--brand-blue); color: var(--white); font-size: 10.5px; font-weight: 600; }
  .top-bar__contact { position: absolute; left: 86px; top: 3px; }
  .top-bar__contact span { margin: 0 8px; font-weight: 400; }
  .top-bar__cart { position: absolute; left: 750px; top: 0; width: 66px; height: 22px; background: var(--white); color: #555; font-size: 11px; display: flex; align-items: center; justify-content: center; gap: 6px; }

  .site-header { position: absolute; left: 0; top: 22px; width: 901px; height: 64px; background: var(--white); box-shadow: 0 2px 4px rgba(0,0,0,.12); z-index: 2; }
  .brand { position: absolute; left: 80px; top: 14px; display: flex; align-items: center; gap: 8px; }
  .brand__mark { width: 26px; height: 26px; border-radius: 50%; background: var(--brand-blue); }
  .brand__name { font-size: 19px; font-weight: 600; color: var(--navy); line-height: 1.05; width: 150px; }
  .main-nav { position: absolute; left: 314px; top: 27px; display: flex; gap: 11px; font-size: 10.6px; color: #222; }
  .main-nav .is-active { color: var(--brand-blue); }

  .hero { position: absolute; left: 0; top: 86px; width: 901px; height: 412px; background: linear-gradient(100deg, #eef1f3 0%, #e2e6e9 40%, #e9c9b4 62%, #e7c2aa 78%, #c7b29d 100%); }
  .hero__title { position: absolute; left: 103px; top: 26px; font-family: "Cinzel", Georgia, serif; color: var(--navy); font-size: 30px; line-height: 36px; letter-spacing: .5px; }
  .hero__title span { display: block; font-size: 32px; }
  .hero__arrow { position: absolute; top: 190px; }
  .hero__arrow--prev { left: 26px; }
  .hero__arrow--next { right: 26px; }
  .hero__dots { position: absolute; left: 427px; top: 393px; display: flex; gap: 4px; }
  .hero__dots i { width: 6px; height: 6px; border-radius: 50%; background: rgba(255,255,255,.7); }
  .hero__dots i.is-active { background: var(--white); }

  .faq { position: absolute; left: 0; top: 498px; width: 901px; height: 364px; background: var(--muted-bg); }
  .section-title { font-family: "Cinzel", Georgia, serif; color: var(--heading-blue); font-size: 24px; text-align: center; letter-spacing: .5px; }
  .faq .section-title { position: absolute; left: 0; top: 18px; width: 901px; }
  .faq__list { position: absolute; left: 114px; top: 78px; width: 670px; }
  .faq__item { margin-bottom: 15px; }
  .faq__q { font-size: 13px; font-weight: 600; color: var(--ink); margin-bottom: 4px; }
  .faq__a { font-size: 10.4px; line-height: 16px; color: var(--body-text); padding-left: 10px; }
  .faq__scroll { position: absolute; left: 815px; top: 566px; }
  .faq__up { position: absolute; left: 441px; top: 323px; }

  .booking { position: absolute; left: 86px; top: 871px; width: 728px; height: 59px; background: linear-gradient(90deg, #1d6e9e, #2c8bc0 45%, #1f78ad); }
  .booking__text { position: absolute; left: 47px; top: 15px; color: var(--white); font-size: 20.5px; font-weight: 600; letter-spacing: .3px; }
  .booking__btn { position: absolute; left: 546px; top: 11px; width: 166px; height: 37px; background: linear-gradient(#8fcf3e, #4e9a20); border: 2px solid #cfe9a6; color: var(--white); font-size: 20px; font-weight: 600; text-align: center; line-height: 32px; }

  .services .section-title { position: absolute; left: 0; top: 954px; width: 901px; }
  .services__see-all { position: absolute; left: 775px; top: 962px; font-size: 10px; font-style: italic; color: #444; }
  .services__rule { position: absolute; left: 96px; top: 993px; width: 708px; height: 1px; background: var(--rule); }
  .service-card { position: absolute; top: 1030px; width: 188px; height: 180px; padding: 0 10px; text-align: center; }
  .service-card.is-featured { border: 1px solid var(--card-border); }
  .service-card__icon { display: block; margin: 14px auto 0; }
  .service-card__title { font-size: 12.5px; color: var(--ink); margin-top: 8px; }
  .service-card__text { font-size: 10.2px; line-height: 14.5px; color: var(--body-text); text-align: justify; margin-top: 5px; }
  .services__arrow { position: absolute; top: 1108px; }
</style>
</head>
<body>

<div class="top-bar">
  <div class="top-bar__contact">(555) 214-7730<span>|</span>Contact us</div>
  <div class="top-bar__cart">
    <svg width="13" height="11" viewBox="0 0 13 11"><path d="M0 1h2l2 6h7l1.5-4.5H3.2" fill="none" stroke="#666" stroke-width="1.3"/><circle cx="5" cy="9.5" r="1.1" fill="#666"/><circle cx="10" cy="9.5" r="1.1" fill="#666"/></svg>
    <span>|</span><span>0</span>
  </div>
</div>

<header class="site-header">
  <div class="brand">
    <span class="brand__mark"></span>
    <span class="brand__name">Bright Oak Family Medicine</span>
  </div>
  <nav class="main-nav">
    <span class="is-active">HOME</span><span>ABOUT US</span><span>SERVICES</span><span>RESOURCES</span><span>FAQs</span><span>CURRENT PATIENTS</span><span>OAKWELL MEMBERSHIP</span><span>STORE</span>
  </nav>
</header>

<section class="hero" role="img" aria-label="Photo of a relaxed woman lying down receiving acupuncture needles on her forehead">
  <h1 class="hero__title">Live Pain Free<span>Experience Acupuncture</span></h1>
  <svg class="hero__arrow hero__arrow--prev" width="16" height="34" viewBox="0 0 16 34"><path d="M14 2L2 17l12 15" fill="none" stroke="#fff" stroke-width="2"/></svg>
  <svg class="hero__arrow hero__arrow--next" width="16" height="34" viewBox="0 0 16 34"><path d="M2 2l12 15L2 32" fill="none" stroke="#fff" stroke-width="2"/></svg>
  <div class="hero__dots"><i></i><i class="is-active"></i><i></i><i></i><i></i></div>
</section>

<section class="faq">
  <h2 class="section-title">Do you have any questions ?</h2>
  <div class="faq__list">
    <div class="faq__item">
      <p class="faq__q">• Do you feel sore or tired at times ?</p>
      <p class="faq__a">Lorem ipsum dolor sit amet, consectetuer adipiscing elit, sed diam nonummy nibh euismod tincidunt ut laoreet dolore magna aliquam erat volutpat. Ut wisi enim ad minim veniam, quis nostrud exerci tation ullamcorper suscipit lobortis nisl ut aliquip ex ea commodo consequat. Duis autem vel eum iriure dolor in hendrerit in vulputate velit esse.</p>
    </div>
    <div class="faq__item">
      <p class="faq__q">• Do you often get headaches ?</p>
      <p class="faq__a">Lorem ipsum dolor sit amet, consectetuer adipiscing elit, sed diam nonummy nibh euismod tincidunt ut laoreet dolore magna aliquam erat volutpat. Ut wisi enim ad minim veniam, quis nostrud exerci tation ullamcorper suscipit lobortis.</p>
    </div>
    <div class="faq__item">
      <p class="faq__q">• Are your museles and joints constantly in pain ?</p>
      <p class="faq__a">Lorem ipsum dolor sit amet, consectetuer adipiscing elit, sed diam nonummy nibh euismod tincidunt ut laoreet dolore magna aliquam erat volutpat. Ut wisi enim ad minim veniam, quis nostrud exerci tation ullamcorper suscipit lobortis.</p>
    </div>
  </div>
  <svg class="faq__up" width="20" height="20" viewBox="0 0 20 20"><circle cx="10" cy="10" r="9" fill="none" stroke="#aaa"/><path d="M6 12l4-4 4 4" fill="none" stroke="#999" stroke-width="1.4"/></svg>
</section>
<svg class="faq__scroll" width="12" height="234" viewBox="0 0 12 234"><rect width="12" height="234" fill="#d4d4d4"/><rect x="1" y="18" width="10" height="30" fill="#a9a9a9"/><path d="M3 218l3-3 3 3M3 226l3 3 3-3" fill="none" stroke="#777"/></svg>

<div class="booking" role="img" aria-label="Banner photo of fresh fruit and vegetables tinted blue">
  <span class="booking__text">BOOK YOUR APPOINTMENT WITH NUTRITION</span>
  <span class="booking__btn">BOOK NOW</span>
</div>

<section class="services">
  <h2 class="section-title">Services we Provide</h2>
  <span class="services__see-all">See All</span>
  <div class="services__rule"></div>

  <svg class="services__arrow" style="left:42px" width="26" height="26" viewBox="0 0 26 26"><circle cx="13" cy="13" r="12" fill="#fff" stroke="#bbb"/><path d="M15 8l-5 5 5 5" fill="none" stroke="#aaa" stroke-width="1.5"/></svg>
  <svg class="services__arrow" style="left:835px" width="26" height="26" viewBox="0 0 26 26"><circle cx="13" cy="13" r="12" fill="#fff" stroke="#999"/><path d="M11 8l5 5-5 5" fill="none" stroke="#777" stroke-width="1.5"/></svg>

  <article class="service-card" style="left:74px">
    <svg class="service-card__icon" width="40" height="40" viewBox="0 0 40 40"><circle cx="13" cy="8" r="5" fill="#3d3d3d"/><circle cx="27" cy="8" r="5" fill="#3d3d3d"/><path d="M6 16h14v12h-3v10h-8V28H6z" fill="#3d3d3d"/><path d="M20 16h14v12h-3v10h-8V28h-3z" fill="#3d3d3d"/><circle cx="20" cy="20" r="3" fill="#3d3d3d"/></svg>
    <h3 class="service-card__title">Integrative Family Medicine</h3>
    <p class="service-card__text">Lorem ipsum dolor sit amet, consectetuer adipiscing elit, sed diam nonummy nibh euismod tincidunt ut laoreet dolore magna aliquam erat volutpat ut wisi enim ad minim veniam quis.</p>
  </article>

  <article class="service-card is-featured" style="left:262px">
    <svg class="service-card__icon" width="44" height="40" viewBox="0 0 44 40"><path d="M6 36C8 18 20 6 40 4 38 24 26 34 10 34z" fill="#8cc63f"/><path d="M4 38C14 26 22 18 34 10" stroke="#fff" stroke-width="2" fill="none"/></svg>
    <h3 class="service-card__title">Functional Medicine</h3>
    <p class="service-card__text">Lorem ipsum dolor sit amet, consectetuer adipiscing elit, sed diam nonummy nibh euismod tincidunt ut laoreet dolore magna aliquam erat volutpat ut wisi enim ad minim veniam quis.</p>
  </article>

  <article class="service-card" style="left:451px">
    <svg class="service-card__icon" width="46" height="40" viewBox="0 0 46 40"><circle cx="15" cy="12" r="7" fill="#3d3d3d"/><circle cx="27" cy="10" r="6" fill="#3d3d3d"/><circle cx="36" cy="15" r="5" fill="#3d3d3d"/><path d="M2 20h42c-2 10-10 16-21 16S4 30 2 20z" fill="#3d3d3d"/></svg>
    <h3 class="service-card__title">Nutrition</h3>
    <p class="service-card__text">Lorem ipsum dolor sit amet, consectetuer adipiscing elit, sed diam nonummy nibh euismod tincidunt ut laoreet dolore magna aliquam erat volutpat ut wisi enim ad minim veniam quis.</p>
  </article>

  <article class="service-card" style="left:641px">
    <svg class="service-card__icon" width="30" height="40" viewBox="0 0 30 40"><circle cx="15" cy="6" r="5" fill="#3d3d3d"/><ellipse cx="15" cy="21" rx="10" ry="10" fill="#3d3d3d"/><rect x="9" y="28" width="5" height="11" fill="#3d3d3d"/><rect x="16" y="28" width="5" height="11" fill="#3d3d3d"/></svg>
    <h3 class="service-card__title">Weight Loss</h3>
    <p class="service-card__text">Lorem ipsum dolor sit amet, consectetuer adipiscing elit, sed diam nonummy nibh euismod tincidunt ut laoreet dolore magna aliquam erat volutpat ut wisi enim ad minim veniam quis.</p>
  </article>
</section>

</body>
</html>
```